Need Business Cards for my Business

email address: rkpmarlowhollowworks@vendrimail.com
web address: rkpmarlowhollowworks.net
Slogan: We offer various QVN licenses
Rowland K. Pemberly
Please stick with colors of Company Logo
would like the card to be more of the color example of the logo.
If you need PDF copy of logo email me at the above account.
Creative control rests with you.

Industry/Entity Type

Business

Contact Information for Business Card

I am a minimalist, but would like something to pop and stand out amongst other cards, make it memorable.

Font styles to use
Serif
Decorative
Script

```html
<!DOCTYPE html>
<html lang="en">
<head>
<meta charset="utf-8">
<title>Marlow Hollow Works – Business Cards</title>
<link rel="stylesheet" href="https://fonts.googleapis.com/css2?family=Arimo:wght@400;700&display=swap">
<style>
  :root {
    --stage: #474747;
    --stage-light: #555555;
    --card-white: #ffffff;
    --blue-light: #1474ba;
    --blue-dark: #13355f;
    --red: #e3222b;
    --red-dark: #c01f2c;
    --ink-blue: #1a5a9c;
    --text-white: #ffffff;
  }
  * { box-sizing: border-box; margin: 0; padding: 0; }
  html, body { width: 999px; height: 1200px; overflow: hidden; }
  body {
    position: relative;
    background: radial-gradient(ellipse at center, var(--stage-light), var(--stage) 75%);
    font-family: "Arimo", Arial, sans-serif;
  }
  .card { position: absolute; left: 53px; width: 892px; height: 509px; overflow: hidden; }

  /* Front card */
  .card-front { top: 83px; background: var(--card-white); }
  .front-brand {
    position: absolute; left: 0; top: 0; width: 444px; height: 100%;
    display: flex; align-items: center; justify-content: center;
  }
  .brand-name {
    font-weight: 700; color: var(--ink-blue); text-transform: uppercase;
    font-size: 34px; line-height: 1.05; letter-spacing: 1px; text-align: left;
  }
  .divider-stripe { position: absolute; left: 444px; top: 0; width: 9px; height: 100%; background: var(--red); }
  .front-panel {
    position: absolute; left: 453px; top: 0; right: 0; height: 100%;
    background: linear-gradient(90deg, var(--blue-light), var(--blue-dark));
  }
  .person-name {
    position: absolute; left: 44px; top: 80px;
    color: var(--text-white); font-weight: 700; font-size: 29px;
  }
  .contact-list { position: absolute; left: -1px; top: 247px; list-style: none; }
  .contact-item { display: flex; align-items: center; height: 35px; margin-bottom: 15px; }
  .contact-icon {
    width: 35px; height: 35px; background: var(--red);
    display: flex; align-items: center; justify-content: center; flex-shrink: 0;
  }
  .contact-text { color: var(--text-white); font-size: 22px; margin-left: 11px; }

  /* Back card */
  .card-back {
    top: 634px;
    background: linear-gradient(90deg, var(--blue-light), var(--blue-dark));
  }
  .back-brand {
    position: absolute; left: 0; right: 0; top: 175px;
    text-align: center; color: var(--text-white); font-weight: 700;
    text-transform: uppercase; font-size: 54px; line-height: 1.05; letter-spacing: 2px;
  }
  .web-band {
    position: absolute; left: 0; right: 0; top: 417px; height: 40px;
    background: linear-gradient(90deg, var(--red), var(--red-dark));
    display: flex; align-items: center; justify-content: center;
  }
  .web-band-text { color: var(--text-white); font-size: 23px; letter-spacing: 4.6px; }
</style>
</head>
<body>

<section class="card card-front">
  <div class="front-brand">
    <div class="brand-name">Marlow Hollow<br>Works</div>
  </div>
  <div class="divider-stripe"></div>
  <div class="front-panel">
    <h1 class="person-name">Rowland K. Pemberly</h1>
    <ul class="contact-list">
      <li class="contact-item">
        <span class="contact-icon">
          <svg width="20" height="20" viewBox="0 0 24 24" aria-hidden="true"><path fill="#fff" d="M6.6 10.8a15 15 0 0 0 6.6 6.6l2.2-2.2c.3-.3.7-.4 1-.2 1.1.4 2.3.6 3.6.6.6 0 1 .4 1 1V20c0 .6-.4 1-1 1A17 17 0 0 1 3 4c0-.6.4-1 1-1h3.5c.6 0 1 .4 1 1 0 1.3.2 2.5.6 3.6.1.3 0 .7-.2 1z"/><path fill="none" stroke="#fff" stroke-width="1.6" d="M14 3a7 7 0 0 1 7 7M14 6.5A3.5 3.5 0 0 1 17.5 10"/></svg>
        </span>
        <span class="contact-text">00 0000 0000</span>
      </li>
      <li class="contact-item">
        <span class="contact-icon">
          <svg width="14" height="20" viewBox="0 0 14 20" aria-hidden="true"><rect x="1.5" y="1.5" width="11" height="17" rx="1.5" fill="none" stroke="#fff" stroke-width="2"/><path d="M4 6l6-2M4 10l6-2" stroke="#fff" stroke-width="1"/></svg>
        </span>
        <span class="contact-text">0000 000 000</span>
      </li>
      <li class="contact-item">
        <span class="contact-icon">
          <svg width="22" height="20" viewBox="0 0 22 20" aria-hidden="true"><path fill="#fff" d="M1 8l10-7 10 7v11H1z"/><path fill="#e3222b" d="M3 9l8 6 8-6-8-5z"/><path fill="none" stroke="#fff" stroke-width="1.4" d="M1 19l8-6M21 19l-8-6"/></svg>
        </span>
        <span class="contact-text">rkpmarlowhollowworks@vendrimail.com</span>
      </li>
      <li class="contact-item">
        <span class="contact-icon">
          <svg width="20" height="20" viewBox="0 0 20 20" aria-hidden="true"><g fill="none" stroke="#fff" stroke-width="1.3"><circle cx="10" cy="10" r="8.5"/><ellipse cx="10" cy="10" rx="3.8" ry="8.5"/><path d="M1.5 10h17M3 5.5h14M3 14.5h14"/></g></svg>
        </span>
        <span class="contact-text">rkpmarlowhollowworks.net</span>
      </li>
    </ul>
  </div>
</section>

<section class="card card-back">
  <div class="back-brand">Marlow Hollow<br>Works</div>
  <div class="web-band"><span class="web-band-text">rkpmarlowhollowworks.net</span></div>
</section>

</body>
</html>
```